Packaging and labelling for Swiss made Organic CBD Oil

Visit our website www.velmoraoils.example
We have not put any product on yet as require packaging and label design .
Website will give you a great feel for the company and how we have used
the logo . The Brastek cbd product shown is a company similar to ourselves with similar core values , we liked the clean packaging design they have .

Im happy if you want use the mandala symbol in our logo separate from
VELMORA, to separate and use the mandala symbol as a larger icon than
it appears in our logo
Clean , Pure , organic feel. Like the product to look pharmaceutical and life changing not gimmicky.
Colours to go with or be the same as our logo colours
But not too cold and clinical
Bottle size 84mm x 25mm
Label size 75mm x 30mm
Box 30mm x 30mm x 100mm
6 products
Full Spectrum :
500mg CBD (5%)
1000mg CBD ( 10% )
1500mg CBD (15%)
2000mg CBD ( 20% )
Broad spectrum THC Free
500mg CBD (5%)
Pets
500mg Broad Spectrum THC Free
Updates

Would like the design to be more modern than traditional

LABEL Information Front of Bottle - Logo VELMORA & Mandala - Mandala can be used separately as design symbol Organic Cannabis Oil 1500mg CBD (15%) Ful Spectrum 10ml Back of bottle Ingredients: Organic Cannabis Oil Extract Organic Sunflower Seed Oil THC - 0.2% Certified Swiss Organic Cultivation Shake well before use. Store in a cool , dry place and out of the each of children BOX information Front and rear Logo - VELMORA & Mandala - Mandala can be used separately as a design symbol Organic Cannabis Oil 1500mg CBD (15%) Full Spectrum Sides x 2 This product is a food supplement and is not intended to diagnose, treat, cure or prevent any disease If you are pregnant, lactating or taking any medication consult your health care practitioner Suitable for vegetarians and vegans Ingredients Organic Cannabis Oil extract Organis Sunflower Oil Store in a cool ,dry place, out of the reach of children Recommended Use 1-5 drops ( 1 drop = 7.5mg CBD ) Subject to body weight and personal requirement - visit www.velmoraoils for more information 100% Natural 100% Organic GMO free 100% Vegan ( symbol with each ) Expiry date see bottle label Cultivated and manufactured in Switzerland

Target Market(s)

age 40 - 80

Font styles to use
Other font styles liked:
• In our website we have used Open Sans for the copy and Lato for headings .

Requirements
Must have
• look like an Industry leader
Velmora will change the quality of peoples lives and in some cases may
even save lives so want look powerful and credible
Our Mission is - Through Delivering Pure , Premium , Organic products we will educate, inform and help people achieve healthier , happier lifestyles
Nice to have
• Colours to look good with our logo colours or be the same as our logo
colours
Logo Font - Avenir Black and Avenir Book

Font used in website - Content - Open Sans / Headings - Lato
If you have another font for the packaging information that will go well with
our logo, I'm happy for you to use your skills

```html
<!DOCTYPE html>
<html lang="en">
<head>
<meta charset="utf-8">
<title>Velmora Cannabis Oil – Label and Box Dieline</title>
<link rel="stylesheet" href="https://fonts.googleapis.com/css2?family=Open+Sans:wght@300;400;600;700&display=swap">
<style>
  :root {
    --paper: #ffffff;
    --ink-black: #0a0a0a;
    --panel-black: #0d0d0d;
    --text-light: #d9d9d9;
    --text-mid: #a6a6a6;
    --text-dim: #8a8a8a;
    --teal: #8fd6d0;
    --guide: #7fd9d9;
    --organic-green: #6cb045;
    --swiss-red: #d6282b;
    --caption: #222222;
  }
  * { margin: 0; padding: 0; box-sizing: border-box; }
  html, body {
    width: 1200px; height: 1000px; overflow: hidden;
    background: var(--paper);
    font-family: "Open Sans", sans-serif;
  }
  .canvas { position: relative; width: 1200px; height: 1000px; overflow: hidden; }
  .dieline {
    position: absolute; left: 15px; top: 0;
    width: 980px; height: 820px;
    transform: scale(1.15); transform-origin: top left;
  }

  .caption {
    position: absolute; font-size: 14px; color: var(--caption);
    transform: translateX(-50%); white-space: nowrap;
  }
  .caption--label { left: 189px; top: 483px; }
  .caption--box { left: 552px; top: 297px; }

  .guide {
    position: absolute; top: 19px; width: 1px; height: 794px;
    background: var(--guide); z-index: 5;
  }

  /* shared dark surface */
  .surface {
    position: absolute; overflow: hidden;
    background: var(--panel-black);
  }
  .surface-glow {
    position: absolute; inset: 0;
    background:
      radial-gradient(ellipse 60px 110px at 30% 20%, rgba(255,255,255,0.07), transparent 70%),
      radial-gradient(ellipse 70px 90px at 80% 60%, rgba(255,255,255,0.05), transparent 70%),
      radial-gradient(ellipse 120px 160px at 50% 45%, rgba(110,130,128,0.10), transparent 75%);
  }

  /* brand block */
  .brand-name {
    position: absolute; font-weight: 600; letter-spacing: 1px;
    color: var(--text-light); white-space: nowrap;
  }
  .organic-line {
    position: absolute; display: flex; align-items: center; gap: 3px;
  }
  .organic-tag {
    background: var(--organic-green); color: #fff; font-weight: 700;
    line-height: 1; padding: 1px 2px; letter-spacing: 0.2px;
  }
  .swiss-square { background: var(--swiss-red); display: block; }
  .badge-plain { background: #e6e6e6; display: block; }
  .product-name {
    position: absolute; font-weight: 300; color: var(--text-light); white-space: nowrap;
  }
  .strength {
    position: absolute; font-weight: 300; color: var(--text-light); line-height: 1.3; white-space: nowrap;
  }
  .origin {
    position: absolute; font-weight: 400; color: var(--text-dim); white-space: nowrap;
  }

  /* bottle label */
  .bottle-label { left: 5px; top: 513px; width: 360px; height: 144px; }
  .bottle-label .brand-name { left: 40px; top: 10px; font-size: 16px; }
  .bottle-label .organic-line { left: 41px; top: 58px; }
  .bottle-label .organic-tag { font-size: 9px; }
  .bottle-label .swiss-square { width: 7px; height: 7px; }
  .bottle-label .badge-plain { width: 10px; height: 8px; }
  .bottle-label .product-name { left: 40px; top: 70px; font-size: 13.5px; }
  .bottle-label .strength { left: 40px; top: 104px; font-size: 9.5px; }
  .label-info {
    position: absolute; left: 157px; top: 140px;
    width: 136px; height: 200px;
    transform: rotate(-90deg); transform-origin: top left;
    display: flex; flex-direction: column; justify-content: flex-start; gap: 5px;
    padding: 4px 2px;
    font-size: 7px; line-height: 1.2; color: var(--text-mid);
  }
  .label-info .label-volume { font-size: 10px; color: var(--text-light); margin-top: 3px; }
  .label-info .label-thc { font-size: 9px; color: var(--text-light); }

  /* box */
  .box-net { position: absolute; left: 403px; top: 328px; width: 576px; height: 480px; display: flex; }
  .box-panel { position: relative; height: 480px; overflow: hidden; }
  .box-panel--wide { width: 145px; }
  .box-panel--narrow { width: 143px; }
  .box-net .surface-glow { pointer-events: none; }

  .box-front .brand-name { left: 23px; top: 36px; font-size: 17px; }
  .box-front .organic-line { left: 16px; top: 234px; }
  .box-front .organic-tag { font-size: 12.5px; }
  .box-front .swiss-square { width: 11px; height: 11px; }
  .box-front .badge-plain { width: 15px; height: 12px; }
  .box-front .product-name { left: 15px; top: 252px; font-size: 19px; }
  .box-front .strength { left: 15px; top: 390px; font-size: 14px; }
  .box-front .origin { left: 15px; top: 452px; font-size: 11.5px; }

  .side-copy {
    position: absolute; left: 10px; right: 8px; top: 180px;
    font-size: 8.4px; line-height: 1.2; color: var(--text-mid);
  }
  .side-copy p { margin-bottom: 6px; }
  .side-copy strong { color: var(--text-light); font-weight: 600; }
  .side-copy .side-heading { color: var(--text-light); font-weight: 600; font-size: 9.5px; margin-bottom: 0; }
  .side-copy .web { color: var(--text-light); font-weight: 600; }
  .volume {
    position: absolute; left: 0; right: 0; text-align: center;
    font-size: 11.5px; color: var(--text-light); font-weight: 300;
  }
  .side-one .volume { top: 453px; }

  .usage-copy {
    position: absolute; left: 10px; right: 8px; top: 20px;
    font-size: 8.2px; line-height: 1.25; color: var(--text-mid);
  }
  .usage-copy .usage-heading { color: var(--teal); font-weight: 600; }
  .usage-copy .web { color: var(--text-light); font-weight: 600; }
  .claims { position: absolute; left: 0; right: 0; top: 124px; }
  .claim {
    position: absolute; left: 0; right: 0; display: flex; flex-direction: column; align-items: center;
  }
  .claim svg { width: 44px; height: 44px; }
  .claim span { font-size: 7.5px; color: var(--teal); font-weight: 600; margin-top: 3px; }
  .claim--natural { top: 0; }
  .claim--organic { top: 72px; }
  .claim--vegan { top: 145px; }
  .claim--gmo { top: 218px; }
  .thc-free {
    position: absolute; left: 0; right: 0; top: 434px; text-align: center;
    font-size: 13px; font-weight: 300; color: var(--text-light);
  }
  .side-two .volume { top: 453px; font-size: 10.5px; }

  .top-flap { left: 691px; top: 25px; width: 288px; height: 287px; }
  .top-flap .brand-name {
    left: 0; right: 0; top: 128px; text-align: center; font-size: 24px; color: var(--teal); letter-spacing: 3px;
  }
</style>
</head>
<body>
<main class="canvas">
  <div class="dieline">

    <p class="caption caption--box">Box sides</p>
    <p class="caption caption--label">Label for bottle</p>

    <!-- bottle label -->
    <section class="surface bottle-label" aria-label="Bottle label">
      <div class="surface-glow" role="img" aria-label="Soft dark background with faint large petal shapes"></div>
      <p class="brand-name">VELMORA</p>
      <div class="organic-line">
        <span class="organic-tag">ORGANIC</span>
        <span class="swiss-square"></span>
        <span class="badge-plain"></span>
      </div>
      <p class="product-name">Cannabis Oil</p>
      <p class="strength">500 mg CBD (5%)<br>Broad Spectrum</p>
      <div class="label-info">
        <p><strong>Ingredients:</strong> Organic Cannabis Oil Extract, Organic Sunflower Oil</p>
        <p>Certified Swiss Organic Cultivation and 100% Natural</p>
        <p class="label-thc">THC free</p>
        <p>Shake well before use. Store in a cool, dry place, out of the reach of children.</p>
        <p><strong>Recommended Use:</strong> 1-5 drops. Subject to body weight and personal requirement – visit www.velmoraoils.example for more information.</p>
        <p class="label-volume">10 ml</p>
      </div>
    </section>

    <!-- box top flap -->
    <section class="surface top-flap" aria-label="Box top">
      <p class="brand-name">VELMORA</p>
    </section>

    <!-- box sides -->
    <section class="box-net" aria-label="Box sides">
      <article class="surface box-panel box-panel--wide box-front">
        <div class="surface-glow" role="img" aria-label="Soft dark background with faint large petal shapes"></div>
        <p class="brand-name">VELMORA</p>
        <div class="organic-line">
          <span class="organic-tag">ORGANIC</span>
          <span class="swiss-square"></span>
          <span class="badge-plain"></span>
        </div>
        <p class="product-name">Cannabis Oil</p>
        <p class="strength">500 mg CBD (5%)<br>Broad Spectrum</p>
        <p class="origin">Made in Switzerland</p>
      </article>

      <article class="surface box-panel box-panel--narrow side-one">
        <div class="surface-glow" role="img" aria-label="Soft dark background with faint large petal shapes"></div>
        <div class="side-copy">
          <p>This product is a food supplement and is not intended to diagnose, treat, cure or prevent any disease.</p>
          <p>If you are pregnant, lactating or taking any medication consult your health care practitioner.</p>
          <p>Suitable for vegetarians and vegans.</p>
          <p><strong>Ingredients:</strong> Organic Cannabis Oil Extract, Organic Sunflower Oil</p>
          <p>Store in a cool, dry place, out of the reach of children.</p>
          <p class="side-heading">Batch No and Lab Results</p>
          <p>Visit <span class="web">www.velmoraoils.example</span> for independent third party lab test results for this product</p>
          <p>Batch No and expiry date see label on bottom of box</p>
        </div>
        <p class="volume">10 ml</p>
      </article>

      <article class="surface box-panel box-panel--narrow box-front">
        <div class="surface-glow" role="img" aria-label="Soft dark background with faint large petal shapes"></div>
        <p class="brand-name">VELMORA</p>
        <div class="organic-line">
          <span class="organic-tag">ORGANIC</span>
          <span class="swiss-square"></span>
          <span class="badge-plain"></span>
        </div>
        <p class="product-name">Cannabis Oil</p>
        <p class="strength">500 mg CBD (5%)<br>Broad Spectrum</p>
        <p class="origin">Made in Switzerland</p>
      </article>

      <article class="surface box-panel box-panel--wide side-two">
        <div class="usage-copy">
          <p class="usage-heading">Recommended Use:</p>
          <p>Shake well before use. 1-5 drops (1 drop = 2.5mg CBD) Subject to body weight and personal requirement – visit <span class="web">www.velmoraoils.example</span> for more information.</p>
        </div>
        <div class="claims">
          <div class="claim claim--natural">
            <svg viewBox="0 0 44 44" aria-hidden="true"><circle cx="22" cy="22" r="20" fill="none" stroke="var(--teal)" stroke-width="2"/></svg>
            <span>100% Natural</span>
          </div>
          <div class="claim claim--organic">
            <svg viewBox="0 0 44 44" aria-hidden="true"><circle cx="22" cy="22" r="20" fill="none" stroke="var(--teal)" stroke-width="2"/></svg>
            <span>100% Organic</span>
          </div>
          <div class="claim claim--vegan">
            <svg viewBox="0 0 44 44" aria-hidden="true"><circle cx="22" cy="22" r="20" fill="none" stroke="var(--teal)" stroke-width="2"/></svg>
            <span>100% Vegan</span>
          </div>
          <div class="claim claim--gmo">
            <svg viewBox="0 0 44 44" aria-hidden="true"><circle cx="22" cy="22" r="20" fill="none" stroke="var(--teal)" stroke-width="2"/></svg>
            <span>GMO Free</span>
          </div>
        </div>
        <p class="thc-free">THC free</p>
        <p class="volume">10 ml</p>
      </article>
    </section>

    <!-- fold and cut guides -->
    <span class="guide" style="left:15px"></span>
    <span class="guide" style="left:159px"></span>
    <span class="guide" style="left:548px"></span>
    <span class="guide" style="left:691px"></span>
    <span class="guide" style="left:834px"></span>
  </div>
</main>
</body>
</html>
```